new KVR one page flyer

We need a 1 page A4 size flyer (need it asap please) that describes on 1 page with art work and using photos the services we provide. I have included some examples of old previous flyers from our other (seperate divisions of the business) I have named a photo called (photo for top of design) however you do your design this photo needs to be the star of the page by either having it at the top or bottom of the page please and we usually like this photo to be in greyscale colour.
we do like greyscale designs but are open to see what you come up with as a whole page of grey white and black might not suit.

Needs to list the following

Services include:
Over size loads / Hot Shot Loads
Heavy Vehicle Recovery services
Potable Water Deliveries
Road Building / Maintenance
Earthworks
Sand & Metal Supply & Cartage
Road Train Tippers
Road Train Tankers
Road Train Flat Tops
Drop Deck Trailers
Mine site accredited equipment & Operators.

We offer a large rage of services not listed so call us today for a personalised quote to suit your needs.

To go on the bottom of the page our contact details are

KVR Pty Ltd
Depot: Lot 514, Banksia Flats Track Coober Pedy
Mobile: 047 216 9381
email: darren@kestrelvaleroadworks.com.au

Target Market(s)

new clients

Colors

Designer to choose colors to be used in the design.

Requirements
Must have
• our services listed
Nice to have
• stand out designs

```html
<!DOCTYPE html>
<html lang="en">
<head>
<meta charset="utf-8">
<title>KVR Flyer</title>
<link href="https://fonts.googleapis.com/css2?family=Roboto:wght@400;500&family=Roboto+Condensed:ital,wght@0,700;1,700;1,800&display=swap" rel="stylesheet">
<style>
  :root{
    --black:#000;
    --gold:#a77b3b;
    --gold-dark:#7d5a26;
    --gold-pill:#9d7337;
    --ink:#111;
    --white:#fff;
    --grey-light:#d9d9d9;
    --grey-mid:#8a8a8a;
    --grey-dark:#3a3a3a;
  }
  *{margin:0;padding:0;box-sizing:border-box}
  html,body{width:927px;height:1200px;overflow:hidden;background:var(--black)}
  .flyer{position:relative;width:927px;height:1200px;overflow:hidden;background:var(--black);font-family:"Roboto",sans-serif}

  .gold-panel{position:absolute;left:88px;top:300px;width:440px;height:900px;
    background:linear-gradient(to bottom,var(--gold) 0,var(--gold) 690px,#3a2a12 820px,var(--black) 900px)}

  .photo-column{position:absolute;left:528px;top:290px;width:399px;height:700px}
  .photo{position:absolute}

  .hero{position:absolute;left:0;top:0;width:927px;height:400px}

  .brand-mark{position:absolute;left:88px;top:46px;width:262px;height:82px;display:flex;align-items:center;
    font-family:"Roboto Condensed",sans-serif;font-weight:700;font-size:86px;color:var(--grey-dark);letter-spacing:2px}
  .divider{position:absolute;left:372px;top:34px;width:2px;height:98px;background:var(--grey-mid)}
  .company-name{position:absolute;left:395px;top:36px;font-family:"Roboto Condensed",sans-serif;font-style:italic;font-weight:800;
    font-size:47px;line-height:1;color:#2b2b2b;white-space:nowrap;letter-spacing:-0.3px}
  .tagline{position:absolute;left:398px;top:91px;font-family:"Roboto Condensed",sans-serif;font-style:italic;font-weight:700;
    font-size:13.4px;line-height:20px;color:#333;text-transform:uppercase}

  .services{position:absolute;left:88px;top:427px;width:440px;list-style:none}
  .services li{height:50px;display:flex;align-items:center;padding-left:20px;
    background:linear-gradient(to right,rgba(0,0,0,0) 55%,rgba(0,0,0,0.14) 100%);
    border-bottom:1px solid rgba(0,0,0,0.18);
    color:var(--white);font-size:23px;font-weight:500}
  .services li.two-line{height:72px;align-items:flex-start;padding-top:6px;line-height:30px;border-bottom:none}
  .tick{width:22px;height:20px;margin-right:12px;flex:none}
  .two-line .tick{margin-top:6px}

  .quote-pill{position:absolute;left:59px;top:1012px;width:560px;height:76px;background:var(--gold-pill);
    border-radius:16px 0 0 16px;padding:12px 0 0 51px;color:var(--ink);font-size:17px;line-height:24px}
  .quote-pill::after{content:"";position:absolute;right:-80px;top:0;width:80px;height:76px;background:var(--gold-pill)}

  .photo-badge{position:absolute;left:606px;top:994px;width:164px;height:164px;border-radius:50%;
    background:var(--gold-pill);padding:9px}
  .photo-badge .photo-inner{width:100%;height:100%;border-radius:50%;
    background:linear-gradient(to bottom,#eef1f3 0,#c9cdd0 45%,#6d6a64 70%,#3e3c39 100%)}
  .truck-photo{position:absolute;left:580px;top:1086px;width:262px;height:92px;border-radius:6px;
    background:linear-gradient(to right,#1f1f1f 0,#3d3a36 40%,#c9c9c9 70%,#e5e5e5 100%);opacity:.9}

  .contact{position:absolute;left:113px;top:1094px;color:var(--white)}
  .contact-name{font-family:"Roboto Condensed",sans-serif;font-weight:700;font-size:17px;line-height:22px;margin-bottom:2px}
  .contact p{font-family:"Roboto Condensed",sans-serif;font-size:13px;line-height:17px;font-weight:400}
</style>
</head>
<body>
<div class="flyer">

  <div class="gold-panel"></div>

  <div class="photo-column">
    <div class="photo" role="img" aria-label="Transportable building loaded on a truck under blue sky"
      style="left:0;top:0;width:399px;height:182px;background:linear-gradient(to bottom,#6f93c4 0,#b3c8e2 45%,#8a6a4a 75%,#8c8478 100%)"></div>
    <div class="photo" role="img" aria-label="Two black prime movers parked side by side, greyscale"
      style="left:0;top:186px;width:399px;height:132px;background:linear-gradient(to right,#2b2b2b 0,#555 50%,#cfcfcf 100%)"></div>
    <div class="photo" role="img" aria-label="Tanker truck on red dirt"
      style="left:0;top:322px;width:184px;height:124px;background:linear-gradient(to bottom,#c9b08a 0,#7a6a5a 50%,#a4562e 100%)"></div>
    <div class="photo" role="img" aria-label="Road train trucks parked in a yard"
      style="left:184px;top:322px;width:215px;height:124px;background:linear-gradient(to bottom,#3f6fb0 0,#9aa7b5 45%,#8d4f2e 100%)"></div>
    <div class="photo" role="img" aria-label="Grader and loader on red earth"
      style="left:0;top:450px;width:220px;height:84px;background:linear-gradient(to bottom,#7b98c8 0,#b8a47a 50%,#a2552c 100%)"></div>
    <div class="photo" role="img" aria-label="Truck hauling oversize portable buildings"
      style="left:220px;top:450px;width:179px;height:84px;background:linear-gradient(to bottom,#9fb3cf 0,#5b5650 55%,#8b5a36 100%)"></div>
    <div class="photo" role="img" aria-label="Low loader carrying a grader"
      style="left:0;top:538px;width:220px;height:68px;background:linear-gradient(to bottom,#3b6aa8 0,#8e8a80 55%,#6d4a2f 100%)"></div>
    <div class="photo" role="img" aria-label="Flat top truck at sunset"
      style="left:220px;top:538px;width:179px;height:68px;background:linear-gradient(to bottom,#c79a86 0,#6d5a55 55%,#3e3432 100%)"></div>
    <div class="photo" role="img" aria-label="Loaders on a flat top road train"
      style="left:0;top:610px;width:399px;height:90px;background:linear-gradient(to bottom,#6f8eb8 0,#8a8c6a 45%,#6e5230 80%,#000 100%)"></div>
  </div>

  <svg class="hero" viewBox="0 0 927 400" role="img" aria-label="Greyscale road train with three tipper trailers on an outback dirt road">
    <defs>
      <linearGradient id="heroTone" x1="0" y1="0" x2="0" y2="1">
        <stop offset="0" stop-color="#e6e6e6"/>
        <stop offset="0.45" stop-color="#cfcfcf"/>
        <stop offset="0.62" stop-color="#6a6a6a"/>
        <stop offset="0.8" stop-color="#9a9a9a"/>
        <stop offset="1" stop-color="#bdbdbd"/>
      </linearGradient>
    </defs>
    <path d="M0,0 H927 V292 C840,290 760,296 700,308 C620,322 560,334 500,348 C440,364 380,380 300,388 C200,396 110,378 0,364 Z" fill="url(#heroTone)"/>
  </svg>

  <div class="brand-mark">KVR</div>
  <div class="divider"></div>
  <h1 class="company-name">KESTREL VALE ROADWORKS</h1>
  <p class="tagline">We specialise in providing services to our customers in some<br>of the most remote locations in Australia</p>

  <ul class="services">
    <li><svg class="tick" viewBox="0 0 22 20"><path d="M2 11 L8 17 L20 2" fill="none" stroke="#111" stroke-width="3.5" stroke-linecap="round" stroke-linejoin="round"/></svg>Over size loads / Hot Shot Loads</li>
    <li><svg class="tick" viewBox="0 0 22 20"><path d="M2 11 L8 17 L20 2" fill="none" stroke="#111" stroke-width="3.5" stroke-linecap="round" stroke-linejoin="round"/></svg>Heavy Vehicle Recovery services</li>
    <li><svg class="tick" viewBox="0 0 22 20"><path d="M2 11 L8 17 L20 2" fill="none" stroke="#111" stroke-width="3.5" stroke-linecap="round" stroke-linejoin="round"/></svg>Potable Water Deliveries</li>
    <li><svg class="tick" viewBox="0 0 22 20"><path d="M2 11 L8 17 L20 2" fill="none" stroke="#111" stroke-width="3.5" stroke-linecap="round" stroke-linejoin="round"/></svg>Road Building / Maintenance</li>
    <li><svg class="tick" viewBox="0 0 22 20"><path d="M2 11 L8 17 L20 2" fill="none" stroke="#111" stroke-width="3.5" stroke-linecap="round" stroke-linejoin="round"/></svg>Earthworks</li>
    <li><svg class="tick" viewBox="0 0 22 20"><path d="M2 11 L8 17 L20 2" fill="none" stroke="#111" stroke-width="3.5" stroke-linecap="round" stroke-linejoin="round"/></svg>Sand &amp; Metal Supply &amp; Cartage</li>
    <li><svg class="tick" viewBox="0 0 22 20"><path d="M2 11 L8 17 L20 2" fill="none" stroke="#111" stroke-width="3.5" stroke-linecap="round" stroke-linejoin="round"/></svg>Road Train Tippers</li>
    <li><svg class="tick" viewBox="0 0 22 20"><path d="M2 11 L8 17 L20 2" fill="none" stroke="#111" stroke-width="3.5" stroke-linecap="round" stroke-linejoin="round"/></svg>Road Train Tankers</li>
    <li><svg class="tick" viewBox="0 0 22 20"><path d="M2 11 L8 17 L20 2" fill="none" stroke="#111" stroke-width="3.5" stroke-linecap="round" stroke-linejoin="round"/></svg>Road Train Flat Tops</li>
    <li><svg class="tick" viewBox="0 0 22 20"><path d="M2 11 L8 17 L20 2" fill="none" stroke="#111" stroke-width="3.5" stroke-linecap="round" stroke-linejoin="round"/></svg>Drop Deck Trailers</li>
    <li class="two-line"><svg class="tick" viewBox="0 0 22 20"><path d="M2 11 L8 17 L20 2" fill="none" stroke="#111" stroke-width="3.5" stroke-linecap="round" stroke-linejoin="round"/></svg><span>Mine site accredited<br>equipment &amp; Operators.</span></li>
  </ul>

  <div class="quote-pill">We offer a large rage of services not listed so<br>call us today for a personalised quote to suit your needs.</div>

  <div class="photo-badge"><div class="photo-inner" role="img" aria-label="Dome shelter workshop with containers"></div></div>
  <div class="truck-photo" role="img" aria-label="Black prime mover and white tanker truck"></div>

  <div class="contact">
    <h2 class="contact-name">KVR Pty Ltd</h2>
    <p>Depot: Lot 514, Banksia Flats Track Coober Pedy</p>
    <p>Mobile: 047 216 9381</p>
    <p>email: darren@kestrelvaleroadworks.com.au</p>
  </div>

</div>
</body>
</html>
```